Plenvoria - Start it your way!

Plenvoria is a new Silicon Valley company, of the kirvel founders from Berlin, which provides a "Open Tandem Weave". This platform allows the crowd to support startups with money, experts and fame. Our Vision is, that everyone should become an entrepreneur.

Pls find all brief details in the attached document
Updates

Would be nice to have a list of more social services I'm available on, like a list of pictograms of all my services:

Find me on: vexlo, ramply+, tqv, brisko, dowmerit, fesk, wumpel, etc...

pls make sure to use the right font:
http://www.lettrovane.com/fonts/Orbitron

Target Market(s)

Main target market is those already involved in the startup industry, by fundraising, investing, advising, cofounding and working. Plenvoria brings a totaly new transparency and collaborative way of starting companies to that business.

· Entrepreneurs (looking for funding, team and community)
· Investors (looking for hot investments and )
· Experts (workers looking for startups they can work for equity)
· Incubators & Business Schools (looking for tools to advise startups)

Industry/Entity Type

It Company

Requirements
Must have
• Pls find all brief details in the attached document
Nice to have

```html
<!DOCTYPE html>
<html lang="en">
<head>
<meta charset="utf-8">
<title>Plenvoria – Business Card</title>
<link rel="stylesheet" href="https://fonts.googleapis.com/css2?family=Orbitron:wght@400;700&family=Open+Sans:wght@400;600&display=swap">
<style>
  :root{
    --page:#ffffff;
    --label:#8a8a8a;
    --band-top:#6e6e6e;
    --paper:#ffffff;
    --accent:#ec6437;
    --ink-light:#f1f1f1;
    --ink-muted:#c9c9c9;
    --ink-dark:#2e2e2e;
    --shadow:rgba(0,0,0,.45);
  }
  html,body{margin:0;padding:0;overflow:hidden;background:var(--page);}
  .sheet{position:relative;width:974px;height:1200px;overflow:hidden;background:var(--page);}
  .side-label{position:absolute;left:90px;margin:0;font:400 28px/1 "Open Sans",sans-serif;color:var(--label);}
  .side-label--recto{top:34px;}
  .side-label--verso{top:620px;}
  .card{position:absolute;left:83px;width:817px;height:475px;display:block;box-shadow:3px 4px 5px var(--shadow);}
  .card--recto{top:88px;}
  .card--verso{top:673px;}
  .orb{font-family:"Orbitron",sans-serif;}
  .sans{font-family:"Open Sans",sans-serif;}
  .url{font-size:12px;fill:var(--ink-muted);}
  .crowd-text{font-family:"Open Sans",sans-serif;font-size:10px;fill:#ffffff;opacity:.06;}
  .brand-name{font-size:31px;fill:var(--ink-muted);font-weight:400;}
  .brand-name--small{font-size:16px;}
  .tagline{font-size:11px;fill:var(--ink-light);}
  .tagline--small{font-size:6px;}
  .person-name{font-size:16px;fill:var(--accent);}
  .person-role{font-size:10.5px;fill:var(--ink-light);}
  .email{font-size:10.5px;fill:var(--accent);}
  .address{font-size:12px;fill:var(--ink-light);}
  .address .city{font-weight:700;}
  .handle{font-size:11px;fill:#5a5a5a;}
  .pitch-lead{font-size:19px;fill:var(--ink-dark);}
  .pitch-item{font-size:22px;fill:var(--ink-light);}
  .notes{font-size:20px;fill:var(--ink-light);}
  .join{font-size:13px;fill:var(--accent);}
</style>
</head>
<body>
<main class="sheet">

  <h2 class="side-label side-label--recto">recto</h2>
  <svg class="card card--recto" viewBox="0 0 743 432" role="group" aria-label="Business card front">
    <defs>
      <linearGradient id="stone" x1="0" y1="0" x2="1" y2="1">
        <stop offset="0" stop-color="#2c2c2c"/>
        <stop offset=".55" stop-color="#3f3f3f"/>
        <stop offset="1" stop-color="#4a4a4a"/>
      </linearGradient>
      <linearGradient id="light-band" x1="0" y1="0" x2="1" y2="0">
        <stop offset="0" stop-color="#a9a9a9"/>
        <stop offset="1" stop-color="#bdbdbd"/>
      </linearGradient>
    </defs>
    <rect class="card-ground" width="743" height="432" fill="url(#stone)" role="img" aria-label="Dark weathered stone texture"/>
    <g class="crowd-pattern">
      <text class="crowd-text" x="0" y="24">founders, backers and builders meet in one open circle where ideas find people, tools and a place to grow together every day</text>
      <text class="crowd-text" x="-20" y="44">share a plan, find a partner, pick a project, join a team and watch small ideas grow into real ventures across two cities</text>
      <text class="crowd-text" x="0" y="64">open circle where ideas find people, tools and a place to grow together. Share a plan, find a partner, pick a project, join</text>
      <text class="crowd-text" x="-30" y="84">builders meet in one open circle. Ideas find people, tools and a place to grow. Founders, backers and builders meet daily</text>
      <text class="crowd-text" x="10" y="104">pick a project, join a team and watch small ideas grow into real ventures across two cities. Founders, backers and builders</text>
      <text class="crowd-text" x="-10" y="124">share a plan, find a partner, pick a project, join a team. Open circle where ideas find people, tools and a place to grow</text>
      <text class="crowd-text" x="0" y="144">a place to grow together every day. Founders, backers and builders meet in one open circle where ideas find people and tools</text>
      <text class="crowd-text" x="-25" y="164">watch small ideas grow into real ventures across two cities. Share a plan, find a partner, pick a project, join a team today</text>
      <text class="crowd-text" x="5" y="184">builders meet in one open circle where ideas find people, tools and a place to grow together. Founders and backers share plans</text>
      <text class="crowd-text" x="-15" y="204">find a partner, pick a project, join a team and watch small ideas grow. Founders, backers and builders meet in one open circle</text>
    </g>
    <path class="band band--top" d="M205 0 H743 V36 C560 28 360 14 205 0 Z" fill="var(--band-top)"/>
    <text class="url orb" x="368" y="23" textLength="347" lengthAdjust="spacing">www.plenvoria.com</text>

    <path class="band band--light" d="M0 212 C250 220 520 240 743 268 V432 H0 Z" fill="url(#light-band)" role="img" aria-label="Light grey textured band"/>
    <path class="band band--paper" d="M0 298 C260 330 520 380 743 432 H0 Z" fill="var(--paper)"/>
    <path class="accent-wedge" d="M585 196 L743 212 L743 268 Z" fill="var(--accent)"/>

    <g class="brand">
      <circle cx="80" cy="92" r="26" fill="var(--accent)"/>
      <text class="brand-name sans" x="56" y="181" textLength="192" lengthAdjust="spacingAndGlyphs">Plenvoria</text>
      <text class="tagline sans" x="149" y="209">Start it your way!</text>
    </g>

    <g class="person">
      <text class="person-name orb" x="366" y="195" textLength="206" lengthAdjust="spacing">Tobias Renwick</text>
      <text class="person-role orb" x="366" y="210" textLength="147" lengthAdjust="spacing">Founder and CEO</text>
      <text class="email orb" x="366" y="242" textLength="289" lengthAdjust="spacing">tre@plenvoria.com</text>
    </g>

    <g class="address orb">
      <text x="366" y="284" textLength="317" lengthAdjust="spacing"><tspan class="city">Berlin</tspan> - Lindenweg 14 |</text>
      <text x="366" y="303" textLength="225" lengthAdjust="spacing">10117 Berlin | Germany</text>
      <text x="366" y="322" textLength="322" lengthAdjust="spacing"><tspan class="city">Silicon Valley</tspan> - 218 Orchard Ave |</text>
      <text x="366" y="339" textLength="219" lengthAdjust="spacing">Sunnyvale | CA 94086</text>
      <text x="366" y="352" textLength="281" lengthAdjust="spacing">T : xxxxxxxxxxxxxxxxxx</text>
    </g>

    <g class="social">
      <rect x="56" y="355" width="28" height="28" rx="3" fill="#8c8c8c"/>
      <rect x="96" y="355" width="28" height="28" rx="3" fill="#7a7a7a"/>
      <rect x="136" y="355" width="28" height="28" rx="3" fill="#6a6a6a"/>
      <text class="handle orb" x="40" y="398" textLength="139" lengthAdjust="spacing">tobiasrenwick</text>
    </g>
  </svg>

  <h2 class="side-label side-label--verso">verso</h2>
  <svg class="card card--verso" viewBox="0 0 743 432" role="group" aria-label="Business card back">
    <defs>
      <linearGradient id="stone-back" x1="0" y1="0" x2="1" y2="1">
        <stop offset="0" stop-color="#2e2e2e"/>
        <stop offset=".6" stop-color="#3d3d3d"/>
        <stop offset="1" stop-color="#555555"/>
      </linearGradient>
      <linearGradient id="swoosh" x1="0" y1="0" x2="1" y2="0">
        <stop offset="0" stop-color="#8e8e8e"/>
        <stop offset=".5" stop-color="#b8b8b8"/>
        <stop offset="1" stop-color="#9a9a9a"/>
      </linearGradient>
      <linearGradient id="swoosh-low" x1="0" y1="0" x2="1" y2="0">
        <stop offset="0" stop-color="#d6d6d6"/>
        <stop offset="1" stop-color="#8a8a8a"/>
      </linearGradient>
    </defs>
    <rect class="card-ground" width="743" height="432" fill="url(#stone-back)" role="img" aria-label="Dark weathered stone texture"/>

    <path class="band band--swoosh" d="M0 48 C260 30 520 30 743 40 V210 C520 170 260 150 0 168 Z" fill="url(#swoosh)"/>
    <path class="band band--paper" d="M0 330 C240 270 500 225 743 205 V222 C500 250 250 310 0 368 Z" fill="url(#swoosh-low)"/>
    <path class="band band--top" d="M205 0 H743 V36 C560 28 360 14 205 0 Z" fill="var(--band-top)"/>
    <text class="url orb" x="372" y="23" textLength="347" lengthAdjust="spacing">www.plenvoria.com</text>

    <g class="crowd-pattern">
      <text class="crowd-text" x="-10" y="44">founders, backers and builders meet in one open circle where ideas find people, tools and a place to grow together every day</text>
      <text class="crowd-text" x="0" y="66">share a plan, find a partner, pick a project, join a team and watch small ideas grow into real ventures across two cities</text>
      <text class="crowd-text" x="-20" y="88">open circle where ideas find people, tools and a place to grow together. Share a plan, find a partner, pick a project, join</text>
      <text class="crowd-text" x="0" y="110">builders meet in one open circle. Ideas find people, tools and a place to grow. Founders, backers and builders meet daily</text>
      <text class="crowd-text" x="-15" y="132">pick a project, join a team and watch small ideas grow into real ventures across two cities. Founders, backers and builders</text>
      <text class="crowd-text" x="5" y="154">share a plan, find a partner, pick a project, join a team. Open circle where ideas find people, tools and a place to grow</text>
      <text class="crowd-text" x="-25" y="176">a place to grow together every day. Founders, backers and builders meet in one open circle where ideas find people and tools</text>
      <text class="crowd-text" x="0" y="198">watch small ideas grow into real ventures across two cities. Share a plan, find a partner, pick a project, join a team today</text>
      <text class="crowd-text" x="-10" y="220">builders meet in one open circle where ideas find people, tools and a place to grow together. Founders and backers share plans</text>
      <text class="crowd-text" x="0" y="242">find a partner, pick a project, join a team and watch small ideas grow. Founders, backers and builders meet in one open circle</text>
      <text class="crowd-text" x="-20" y="264">founders, backers and builders meet in one open circle where ideas find people, tools and a place to grow together every day</text>
      <text class="crowd-text" x="0" y="286">share a plan, find a partner, pick a project, join a team and watch small ideas grow into real ventures across two cities</text>
      <text class="crowd-text" x="-10" y="308">open circle where ideas find people, tools and a place to grow together. Share a plan, find a partner, pick a project, join</text>
      <text class="crowd-text" x="0" y="330">builders meet in one open circle. Ideas find people, tools and a place to grow. Founders, backers and builders meet daily</text>
      <text class="crowd-text" x="-15" y="352">pick a project, join a team and watch small ideas grow into real ventures across two cities. Founders, backers and builders</text>
      <text class="crowd-text" x="0" y="374">share a plan, find a partner, pick a project, join a team. Open circle where ideas find people, tools and a place to grow</text>
      <text class="crowd-text" x="-20" y="396">a place to grow together every day. Founders, backers and builders meet in one open circle where ideas find people and tools</text>
      <text class="crowd-text" x="0" y="418">watch small ideas grow into real ventures across two cities. Share a plan, find a partner, pick a project, join a team today</text>
    </g>

    <g class="pitch orb">
      <text class="pitch-lead" x="53" y="92" textLength="355" lengthAdjust="spacing">Are you interested in</text>
      <text class="pitch-item" x="82" y="121" textLength="150" lengthAdjust="spacing">Startups,</text>
      <text class="pitch-item" x="153" y="148" textLength="215" lengthAdjust="spacing">Investments,</text>
      <text class="pitch-item" x="314" y="171" textLength="102" lengthAdjust="spacing">Work?</text>
    </g>

    <g class="notes orb">
      <text x="47" y="253" textLength="423" lengthAdjust="spacing">notesxxxxxxxxxxxxxxxxx</text>
      <text x="47" y="281" textLength="288" lengthAdjust="spacing">xxxxxxxxxxxxxxx</text>
      <text x="47" y="309" textLength="245" lengthAdjust="spacing">xxxxxxxxxxxx</text>
    </g>

    <g class="brand">
      <circle cx="620" cy="322" r="24" fill="var(--accent)"/>
      <text class="brand-name brand-name--small sans" x="557" y="384" textLength="118" lengthAdjust="spacingAndGlyphs">Plenvoria</text>
      <text class="tagline tagline--small sans" x="614" y="398">Start it your way!</text>
    </g>

    <text class="join orb" x="40" y="400" textLength="336" lengthAdjust="spacing">Join: Hublio.com/Plenvoria</text>
  </svg>

</main>
</body>
</html>
```